Modern Business Card

Modern professional business card with more than just logo and demographic info. Something memorable.

We are a trendy/modern chiropractic group with an emphasis on neurology, hence the minimalist-type brain logo. We want to convey that modern and technical aspect with professionalism and the elite nature of our practice environment.

```html
<!DOCTYPE html>
<html lang="en">
<head>
<meta charset="utf-8">
<title>Cadence Chiropractic — Business Card</title>
<link rel="stylesheet" href="https://fonts.googleapis.com/css2?family=Cinzel:wght@500&family=Open+Sans:wght@400;600&display=swap">
<style>
  :root {
    --stage: #1d1d1d;
    --stage-light: #2c2c2c;
    --card-black: #0b0b0b;
    --pattern-dark: #141414;
    --pattern-light: #1c1c1c;
    --paper: #ffffff;
    --ink: #1a1a1a;
    --ink-soft: #555555;
    --accent: #4680c2;
    --ring: #5a5a5a;
  }
  * { margin: 0; padding: 0; box-sizing: border-box; }
  html, body { width: 1200px; height: 900px; overflow: hidden; }
  body {
    background: radial-gradient(circle at 60% 30%, var(--stage-light), var(--stage) 70%);
    position: relative;
    font-family: "Open Sans", sans-serif;
  }
  .card {
    position: absolute;
    left: 290px;
    width: 620px;
    height: 354px;
    overflow: hidden;
    box-shadow: 0 14px 30px rgba(0,0,0,.55);
  }
  /* Back side */
  .card-back { top: 76px; background: var(--card-black); }
  .card-back .pattern-field {
    position: absolute; inset: 0;
    background: linear-gradient(135deg, var(--pattern-light), var(--pattern-dark) 50%, var(--pattern-light));
  }
  .card-back .brand-block {
    position: absolute; left: 0; right: 0; top: 90px;
    text-align: center; color: var(--paper);
    font-family: "Cinzel", serif; font-weight: 500;
  }
  .brand-dot {
    width: 34px; height: 34px; border-radius: 50%;
    background: var(--accent); margin: 0 auto 70px;
  }
  .card-back .brand-name { font-size: 30px; line-height: 1; letter-spacing: 1px; }
  .card-back .brand-sub { font-size: 15px; line-height: 1.1; letter-spacing: 1px; }

  /* Front side */
  .card-front { top: 470px; background: var(--paper); }
  .accent-disc { position: absolute; inset: 0; }
  .front-brand {
    position: absolute; left: 48px; top: 36px;
    font-family: "Cinzel", serif; font-weight: 500; color: var(--ink);
  }
  .front-brand .brand-name { font-size: 38px; line-height: 1; letter-spacing: 1px; }
  .front-brand .brand-sub { font-size: 19px; line-height: 1; letter-spacing: 1px; margin-top: -2px; }
  .person { position: absolute; left: 56px; top: 140px; }
  .person-name {
    font-family: "Cinzel", serif; font-weight: 500;
    font-size: 25px; color: var(--ink-soft); letter-spacing: .5px;
  }
  .person-role { font-size: 17px; color: var(--accent); margin-top: -2px; }
  .divider {
    position: absolute; left: 50px; top: 214px;
    width: 250px; height: 2px; background: var(--ink);
  }
  .contact-list {
    position: absolute; left: 48px; top: 230px;
    list-style: none; font-size: 18px; color: var(--ink-soft);
  }
  .contact-list li { display: flex; align-items: center; gap: 10px; height: 28px; }
  .contact-list svg { width: 18px; height: 18px; flex: none; }
  .contact-list .web-strong { color: var(--accent); font-weight: 600; }
  .disc-name {
    position: absolute; left: 420px; top: 170px; width: 200px;
    text-align: center; color: var(--paper);
    font-family: "Cinzel", serif; font-weight: 500; font-size: 30px; letter-spacing: 1px;
  }
</style>
</head>
<body>

<section class="card card-back">
  <div class="pattern-field" role="img" aria-label="Repeating tonal pattern of the practice emblem across the dark card back"></div>
  <div class="brand-block">
    <div class="brand-dot"></div>
    <div class="brand-name">CADENCE</div>
    <div class="brand-sub">CHIROPRACTIC</div>
  </div>
</section>

<section class="card card-front">
  <svg class="accent-disc" viewBox="0 0 620 354" aria-hidden="true">
    <circle cx="625" cy="190" r="240" fill="var(--ring)"/>
    <circle cx="631" cy="190" r="236" fill="var(--accent)"/>
  </svg>
  <div class="disc-name">CADENCE</div>

  <div class="front-brand">
    <div class="brand-name">CADENCE</div>
    <div class="brand-sub">CHIROPRACTIC</div>
  </div>

  <div class="person">
    <div class="person-name">DANIEL REEVE</div>
    <div class="person-role">Training Specialist</div>
  </div>
  <div class="divider"></div>

  <ul class="contact-list">
    <li>
      <svg viewBox="0 0 24 24" fill="none" stroke="var(--accent)" stroke-width="2"><circle cx="12" cy="12" r="10"/><path d="M8 7l2 0 1 3-1.5 1a6 6 0 0 0 3.5 3.5l1-1.5 3 1v2a2 2 0 0 1-2 1A9 9 0 0 1 7 9a2 2 0 0 1 1-2z"/></svg>
      555.014.2290
    </li>
    <li>
      <svg viewBox="0 0 24 24" fill="none" stroke="var(--accent)" stroke-width="2"><rect x="2" y="5" width="20" height="14"/><path d="M2 5l10 8 10-8"/></svg>
      d.reeve@cadencechiro.com
    </li>
    <li>
      <svg viewBox="0 0 24 24" fill="none" stroke="var(--accent)" stroke-width="2"><circle cx="12" cy="12" r="10"/><path d="M2 12h20M12 2c3 3 3 17 0 20M12 2c-3 3-3 17 0 20"/></svg>
      <span>www.<span class="web-strong">cadencechiro</span>.com</span>
    </li>
  </ul>
</section>

</body>
</html>
```